Copper lark buildworks

Copper lark buildworks is a small construction company.
Who is a licenced builder, Carpenter, joiner,
working on heritage ,new build, speacial projects and sometimes furniture

Industry/Entity Type

Construction

```html
<!DOCTYPE html>
<html lang="en">
<head>
<meta charset="utf-8">
<title>Copper lark buildworks – Business Card</title>
<link href="https://fonts.googleapis.com/css2?family=Open+Sans:wght@400;600&family=Roboto+Slab:wght@400;500&display=swap" rel="stylesheet">
<style>
  :root {
    --backdrop: #e9e7e4;
    --card-white: #ffffff;
    --brand-green: #15a800;
    --panel-dark: #333333;
    --ink-dark: #333333;
    --ink-light: #ffffff;
  }
  * { margin: 0; padding: 0; box-sizing: border-box; }
  html, body {
    width: 1200px; height: 900px; overflow: hidden;
    background: var(--backdrop);
  }
  .canvas { position: relative; width: 1200px; height: 900px; }

  .card { position: absolute; overflow: hidden; box-shadow: 0 4px 14px rgba(0,0,0,.18); }

  /* Front card */
  .card-front { left: 78px; top: 33px; width: 588px; height: 364px; background: var(--card-white); }
  .card-front .shapes { position: absolute; inset: 0; }
  .brand-mark {
    position: absolute; left: 0; right: 0; top: 62px;
    display: flex; justify-content: center; align-items: center; gap: 12px;
  }
  .brand-mark .mark-square { width: 26px; height: 26px; background: var(--brand-green); }
  .brand-mark .mark-name {
    font-family: "Roboto Slab", Georgia, serif; font-weight: 500;
    font-size: 30px; color: var(--brand-green); letter-spacing: .2px;
  }
  .company-name {
    position: absolute; left: 0; right: 0; top: 141px; text-align: center;
    font-family: "Roboto Slab", Georgia, serif; font-weight: 400;
    font-size: 23px; color: var(--ink-dark);
  }
  .contact-list {
    position: absolute; left: 30px; top: 256px; list-style: none;
    font-family: "Open Sans", Arial, sans-serif; font-size: 15px; color: var(--ink-light);
  }
  .contact-list li { display: flex; align-items: center; gap: 8px; height: 21.5px; }
  .contact-list svg { width: 12px; height: 12px; fill: var(--ink-light); flex: none; }
  .person {
    position: absolute; right: 36px; top: 234px; text-align: right; color: var(--ink-light);
  }
  .person-name { font-family: "Roboto Slab", Georgia, serif; font-size: 24px; line-height: 30px; }
  .person-title { font-family: "Open Sans", Arial, sans-serif; font-size: 15.5px; line-height: 22px; }
  .person-address {
    margin-top: 8px; font-family: "Open Sans", Arial, sans-serif; font-size: 15px; line-height: 22px;
  }

  /* Back card */
  .card-back { left: 388px; top: 505px; width: 566px; height: 352px; background: var(--brand-green); }
  .card-back .brand-mark { top: 158px; }
  .card-back .mark-square { background: var(--ink-light); }
  .card-back .mark-name { color: var(--ink-light); font-size: 32px; }
  .back-website {
    position: absolute; left: 0; right: 0; top: 293px; text-align: center;
    font-family: "Open Sans", Arial, sans-serif; font-size: 15px; color: var(--ink-light);
  }
</style>
</head>
<body>
<main class="canvas">

  <section class="card card-front" aria-label="Business card front">
    <svg class="shapes" width="588" height="364" viewBox="0 0 588 364" aria-hidden="true">
      <polygon points="0,197 372,197 352,222 0,222" fill="var(--brand-green)"/>
      <polygon points="0,226 356,226 386,187 588,187 588,364 0,364" fill="var(--panel-dark)"/>
    </svg>

    <div class="brand-mark">
      <span class="mark-square"></span>
      <span class="mark-name">Copper lark buildworks</span>
    </div>
    <p class="company-name">Copper lark buildworks</p>

    <ul class="contact-list">
      <li>
        <svg viewBox="0 0 12 12"><path d="M3 0h6a1 1 0 0 1 1 1v10a1 1 0 0 1-1 1H3a1 1 0 0 1-1-1V1a1 1 0 0 1 1-1zm0 1.5v7.5h6V1.5zm3 8.4a.7.7 0 1 0 0 1.4.7.7 0 0 0 0-1.4z"/></svg>
        061-482 730 915
      </li>
      <li>
        <svg viewBox="0 0 12 12"><path d="M1 3.5C1 2 3 1 6 1s5 1 5 2.5V5H8.5V3.8C8 3.4 7 3.2 6 3.2s-2 .2-2.5.6V5H1zM3 6h6l1.5 5h-9zm3 1.2a1.5 1.5 0 1 0 0 3 1.5 1.5 0 0 0 0-3z"/></svg>
        061-482 730 915
      </li>
      <li>
        <svg viewBox="0 0 12 12"><path d="M0 2h12v8H0zm1.2 1.2v.4L6 6.8l4.8-3.2v-.4zm0 1.8v3.8h9.6V5L6 8.2z"/></svg>
        hello@copperlark.com
      </li>
      <li>
        <svg viewBox="0 0 12 12"><circle cx="6" cy="6" r="5.5"/><path d="M6 .5v11M.5 6h11M2.5 2.5c2 1.3 5 1.3 7 0M2.5 9.5c2-1.3 5-1.3 7 0" stroke="var(--panel-dark)" stroke-width=".8" fill="none"/></svg>
        www.copperlark.com
      </li>
    </ul>

    <div class="person">
      <p class="person-name">Elias Marwood</p>
      <p class="person-title">Managing Director</p>
      <p class="person-address">27 Foundry Lane, Millbrook<br>Ashford Vale, 482913.</p>
    </div>
  </section>

  <section class="card card-back" aria-label="Business card back">
    <div class="brand-mark">
      <span class="mark-square"></span>
      <span class="mark-name">Copper lark buildworks</span>
    </div>
    <p class="back-website">www.copperlark.com</p>
  </section>

</main>
</body>
</html>
```